Help! We need PROFESSIONAL E-mail Signatures that POP!

9/12 UPDATE:
We have extended the deadline.
Also the logo we want used for Melsford has changed.

We have 8 employees working for three companies. We want our e-mail signatures to be the same format and cohesive, but each person has one company of the three that needs to be highlighted.
- Logos are attached and spreadsheet shows what information is needed for each employee as well as which of the logos should be the primary logo - first one displayed and slightly larger than the others.
- Please create one design first using the information for Daniel Wystan from Line 2 of the spreadsheet (provided three versions - Numbers, Excel, PDF
- All components need to be able to be changed or deleted.
- We need to be able to easily create new signatures for new employees
Updates

Need extra days to review

If you submitted a design prior to yesterday afternoon, please see original brief for the updated Melsford logo. This is the version of the Melsford logo that will be used for all the email signatures. The spreadsheet with the info for all 8 employees show different versions of this logo for different employees. Ignore that. Use this one logo in the design along with the Pelna and Brisk logos as indicated on the spreadsheet. Thanks!

Target Market(s)

New/existing clients!

Industry/Entity Type

Property development, commercial construction, property management

Font styles to use
Sans Serif

Requirements
Must have
• A lot of info with a clean look
Nice to have
• Consistency and cohesion
Should not have
• Too many elements - UPDATE: No photos - thanks!

```html
<!DOCTYPE html>
<html lang="en">
<head>
<meta charset="utf-8">
<title>Melsford Email Signatures</title>
<link href="https://fonts.googleapis.com/css2?family=Noto+Sans:wght@400;500;600&display=swap" rel="stylesheet">
<style>
  :root {
    --backdrop: #8c8c8c;
    --card: #ffffff;
    --green: #72bf44;
    --ink: #3d3d3d;
    --rule: #cfcfcf;
  }
  * { margin: 0; padding: 0; box-sizing: border-box; }
  html, body { width: 864px; height: 1200px; overflow: hidden; }
  body {
    background: var(--backdrop);
    font-family: "Noto Sans", Arial, sans-serif;
    color: var(--ink);
    position: relative;
  }
  .signature {
    position: absolute;
    left: 85px;
    width: 682px;
    height: 321px;
    background: var(--card);
  }
  .signature > * { position: absolute; }

  /* brand block */
  .brand { left: 23px; width: 132px; }
  .brand-mark { display: flex; align-items: center; gap: 8px; }
  .brand-square { width: 32px; height: 32px; background: var(--green); flex: none; }
  .brand-name { font-size: 18px; font-weight: 500; color: var(--ink); line-height: 22px; }
  .partners {
    display: flex; align-items: center; justify-content: space-between;
    margin-top: 18px; width: 132px;
  }
  .partner-name { font-size: 13px; font-weight: 600; color: var(--ink); }
  .partner-divider { width: 1px; height: 28px; background: var(--rule); }

  .divider { left: 182px; width: 1px; background: var(--rule); }

  .person { left: 206px; }
  .person-name { font-size: 20px; color: var(--green); line-height: 23px; letter-spacing: 0.4px; white-space: nowrap; }
  .person-title { font-size: 12px; line-height: 15px; letter-spacing: 0.3px; color: var(--ink); white-space: nowrap; }

  .icon {
    left: 408px; width: 17px; height: 17px;
    border: 1.3px solid var(--green);
    display: flex; align-items: center; justify-content: center;
  }
  .icon svg { width: 8px; height: 8px; fill: var(--ink); }
  .contact-rule { left: 436px; width: 1px; background: var(--rule); }
  .contact {
    left: 444px; font-size: 14.5px; line-height: 17px; letter-spacing: 0.4px;
    white-space: nowrap; color: var(--ink);
  }
  .contact .label { color: var(--green); }

  .web-band {
    left: 23px; width: 636px; height: 26px;
    background: var(--green);
    display: flex; align-items: center; justify-content: space-between;
    padding: 0 8px 0 16px;
  }
  .web-address { font-size: 19px; color: var(--ink); line-height: 26px; letter-spacing: 0.3px; }
  .social { display: flex; gap: 11px; }
  .social-square { width: 17px; height: 17px; background: var(--ink); border-radius: 2px; }

  .notice {
    left: 23px; width: 636px;
    font-size: 8.4px; line-height: 9.6px;
    text-align: justify; text-align-last: left;
    color: var(--ink);
  }
  .notice .label { color: var(--green); }
</style>
</head>
<body>

<svg width="0" height="0" style="position:absolute">
  <defs>
    <symbol id="glyph-phone" viewBox="0 0 10 10"><path d="M2.2 0.6 3.6 2.3 2.8 3.3C3.4 4.7 5.3 6.6 6.7 7.2L7.7 6.4 9.4 7.8 8.4 9.4C4.8 9.2 0.8 5.2 0.6 1.6Z"/></symbol>
    <symbol id="glyph-mail" viewBox="0 0 10 10"><path d="M0.5 2H9.5V8H0.5ZM1.3 2.6 5 5.4 8.7 2.6Z"/></symbol>
    <symbol id="glyph-pin" viewBox="0 0 10 10"><path d="M5 0.4A3.3 3.3 0 0 0 1.7 3.7C1.7 6.2 5 9.6 5 9.6S8.3 6.2 8.3 3.7A3.3 3.3 0 0 0 5 0.4ZM5 2.4A1.3 1.3 0 1 1 5 5A1.3 1.3 0 1 1 5 2.4Z"/></symbol>
  </defs>
</svg>

<!-- Daniel Wystan -->
<section class="signature" style="top:88px">
  <div class="brand" style="top:73px">
    <div class="brand-mark">
      <div class="brand-square"></div>
      <span class="brand-name">Melsford</span>
    </div>
    <div class="partners">
      <span class="partner-name">Pelna</span>
      <span class="partner-divider"></span>
      <span class="partner-name">Brisk</span>
    </div>
  </div>
  <div class="divider" style="top:44px;height:144px"></div>
  <div class="person" style="top:89px">
    <p class="person-name">Daniel Wystan</p>
    <p class="person-title">CEO/Owner</p>
  </div>

  <div class="icon" style="top:45px"><svg><use href="#glyph-phone"/></svg></div>
  <div class="icon" style="top:93px"><svg><use href="#glyph-mail"/></svg></div>
  <div class="icon" style="top:121px"><svg><use href="#glyph-pin"/></svg></div>
  <div class="contact-rule" style="top:44px;height:40px"></div>
  <div class="contact-rule" style="top:93px;height:17px"></div>
  <div class="contact-rule" style="top:121px;height:67px"></div>

  <p class="contact" style="top:42px"><span class="label">Direct:</span> 555-201-4417</p>
  <p class="contact" style="top:67px"><span class="label">Melsford:</span> 555-310-7700 x101</p>
  <p class="contact" style="top:92px">dwystan@melsford.com</p>
  <p class="contact" style="top:117px"><span class="label">IL RE Lic#:</span> 471.009318</p>
  <p class="contact" style="top:133px"><span class="label">Chicago GC Lic #:</span> TGC058316</p>
  <p class="contact" style="top:158px">18 N. Linden Ave., Ste 4B,<br>Ferncroft IL 60599</p>

  <div class="web-band" style="top:228px">
    <span class="web-address">www.melsford.com</span>
    <div class="social"><span class="social-square"></span><span class="social-square"></span><span class="social-square"></span></div>
  </div>
  <p class="notice" style="top:263px"><span class="label">CONFIDENTIALITY NOTICE:</span> This e-mail is intended only for the recipient named and may contain confidential, privileged, and exempt from disclosure under applicable laws. If you are not the named recipient, you may have received this transmission in error. We ask that you, please immediately notify us by e-mail at operations@melsford.com and remove this and all attached file(s) from your system. You are notified that any disclosure, copying, distribution, or use of the information in this transmission if you are not the intended recipient is prohibited and may expose you to liability.</p>
</section>

<!-- Owen Tallis -->
<section class="signature" style="top:435px">
  <div class="brand" style="top:93px">
    <div class="brand-mark">
      <div class="brand-square"></div>
      <span class="brand-name">Melsford</span>
    </div>
  </div>
  <div class="divider" style="top:45px;height:128px"></div>
  <div class="person" style="top:89px">
    <p class="person-name">Owen Tallis</p>
    <p class="person-title">Head of Development</p>
  </div>

  <div class="icon" style="top:46px"><svg><use href="#glyph-phone"/></svg></div>
  <div class="icon" style="top:94px"><svg><use href="#glyph-mail"/></svg></div>
  <div class="icon" style="top:122px"><svg><use href="#glyph-pin"/></svg></div>
  <div class="contact-rule" style="top:45px;height:40px"></div>
  <div class="contact-rule" style="top:94px;height:17px"></div>
  <div class="contact-rule" style="top:122px;height:52px"></div>

  <p class="contact" style="top:43px"><span class="label">Direct:</span> 555-201-4452</p>
  <p class="contact" style="top:68px"><span class="label">Melsford:</span> 555-310-7700 x103</p>
  <p class="contact" style="top:93px">development@melsford.com</p>
  <p class="contact" style="top:118px"><span class="label">Chicago GC Lic#:</span> TGC058316</p>
  <p class="contact" style="top:143px">18 N. Linden Ave., Ste 4B,<br>Ferncroft IL 60599</p>

  <div class="web-band" style="top:229px">
    <span class="web-address">www.melsford.com</span>
    <div class="social"><span class="social-square"></span><span class="social-square"></span><span class="social-square"></span></div>
  </div>
  <p class="notice" style="top:264px"><span class="label">CONFIDENTIALITY NOTICE:</span> This e-mail is intended only for the recipient named and may contain confidential, privileged, and exempt from disclosure under applicable laws. If you are not the named recipient, you may have received this transmission in error. We ask that you, please immediately notify us by e-mail at operations@melsford.com and remove this and all attached file(s) from your system. You are notified that any disclosure, copying, distribution, or use of the information in this transmission if you are not the intended recipient is prohibited and may expose you to liability.</p>
</section>

<!-- Clara Pendell -->
<section class="signature" style="top:783px">
  <div class="brand" style="top:92px">
    <div class="brand-mark">
      <div class="brand-square"></div>
      <span class="brand-name">Melsford</span>
    </div>
  </div>
  <div class="divider" style="top:44px;height:129px"></div>
  <div class="person" style="top:89px">
    <p class="person-name">Clara Pendell</p>
    <p class="person-title">Development Manager</p>
  </div>

  <div class="icon" style="top:45px"><svg><use href="#glyph-phone"/></svg></div>
  <div class="icon" style="top:93px"><svg><use href="#glyph-mail"/></svg></div>
  <div class="icon" style="top:121px"><svg><use href="#glyph-pin"/></svg></div>
  <div class="contact-rule" style="top:44px;height:40px"></div>
  <div class="contact-rule" style="top:93px;height:17px"></div>
  <div class="contact-rule" style="top:121px;height:52px"></div>

  <p class="contact" style="top:42px"><span class="label">Direct:</span> 555-201-4489</p>
  <p class="contact" style="top:67px"><span class="label">Melsford:</span> 555-310-7700 x102</p>
  <p class="contact" style="top:92px">projects@melsford.com</p>
  <p class="contact" style="top:117px"><span class="label">Chicago GC Lic#:</span> TGC058316</p>
  <p class="contact" style="top:142px">18 N. Linden Ave., Ste 4B,<br>Ferncroft IL 60599</p>

  <div class="web-band" style="top:228px">
    <span class="web-address">www.melsford.com</span>
    <div class="social"><span class="social-square"></span><span class="social-square"></span><span class="social-square"></span></div>
  </div>
  <p class="notice" style="top:263px"><span class="label">CONFIDENTIALITY NOTICE:</span> This e-mail is intended only for the recipient named and may contain confidential, privileged, and exempt from disclosure under applicable laws. If you are not the named recipient, you may have received this transmission in error. We ask that you, please immediately notify us by e-mail at operations@melsford.com and remove this and all attached file(s) from your system. You are notified that any disclosure, copying, distribution, or use of the information in this transmission if you are not the intended recipient is prohibited and may expose you to liability.</p>
</section>

</body>
</html>
```